Torvane PT Business Card

I need the card to be bright/bold colours to stand out amongst others.
It needs to have my company logo.
I was not interested in pictures etc just a layout that attracts attention.

I have attached my old design which is very plain. I also needed change the contact details. And my description changed to Personal Trainer
Phone 0427309581
Facebook Torvane PT
No email address please, no street address.
And only Torvane PT (Please remove anything to do with Torvane Supplements)

```html
<!DOCTYPE html>
<html lang="en">
<head>
<meta charset="utf-8">
<title>Torvane PT Business Card</title>
<link rel="stylesheet" href="https://fonts.googleapis.com/css2?family=Ubuntu:wght@400;500;700&display=swap">
<style>
  :root {
    --backdrop: #4b4b4b;
    --card: #ffffff;
    --brand-blue: #1a8fd1;
    --brand-yellow: #f7d812;
    --text-grey: #5a5a5a;
  }
  * { box-sizing: border-box; margin: 0; padding: 0; }
  html, body {
    width: 1200px;
    height: 900px;
    overflow: hidden;
    background: var(--backdrop);
    font-family: "Ubuntu", sans-serif;
  }
  .stage {
    width: 1200px;
    height: 900px;
    display: flex;
    align-items: center;
    justify-content: center;
  }
  .business-card {
    position: relative;
    width: 900px;
    height: 514px;
    background: var(--card);
    border-radius: 46px;
    box-shadow: 0 18px 40px rgba(0,0,0,0.35);
    display: flex;
    align-items: center;
    padding: 0 0 0 90px;
  }
  .brand {
    width: 300px;
    display: flex;
    flex-direction: column;
    align-items: flex-end;
  }
  .brand-name {
    display: flex;
    align-items: center;
    gap: 12px;
    font-weight: 700;
    font-size: 48px;
    color: var(--brand-blue);
    letter-spacing: 1px;
    white-space: nowrap;
  }
  .brand-dot {
    width: 18px;
    height: 18px;
    border-radius: 50%;
    background: var(--brand-yellow);
  }
  .brand-rule {
    width: 100%;
    height: 2px;
    background: var(--brand-blue);
    margin-top: 14px;
  }
  .divider {
    width: 1.5px;
    height: 210px;
    background: var(--brand-blue);
    margin: 0 46px 0 40px;
  }
  .details {
    display: flex;
    flex-direction: column;
  }
  .person-name {
    font-weight: 700;
    font-size: 38px;
    letter-spacing: 0.5px;
    color: var(--brand-blue);
    line-height: 1.05;
  }
  .person-name .surname { color: var(--brand-yellow); }
  .person-role {
    font-size: 24px;
    color: var(--text-grey);
    letter-spacing: 0.5px;
    margin-top: 6px;
  }
  .contact-list {
    list-style: none;
    margin-top: 22px;
  }
  .contact-item {
    display: flex;
    align-items: center;
    gap: 22px;
    font-size: 22px;
    color: var(--text-grey);
    margin-top: 10px;
  }
  .contact-icon {
    width: 22px;
    height: 22px;
    flex: none;
  }
  .social-mark {
    width: 20px;
    height: 20px;
    border-radius: 50%;
    background: var(--brand-blue);
    flex: none;
    margin: 0 1px;
  }
</style>
</head>
<body>
<main class="stage">
  <article class="business-card">
    <div class="brand">
      <div class="brand-name"><span class="brand-dot"></span>Torvane PT</div>
      <div class="brand-rule"></div>
    </div>
    <div class="divider"></div>
    <div class="details">
      <h1 class="person-name">DANA <span class="surname">MERCER</span></h1>
      <p class="person-role">PERSONAL TRAINER</p>
      <ul class="contact-list">
        <li class="contact-item">
          <svg class="contact-icon" viewBox="0 0 24 24" aria-hidden="true">
            <path fill="#1a8fd1" d="M6.6 10.8c1.4 2.8 3.8 5.1 6.6 6.6l2.2-2.2c.3-.3.7-.4 1-.2 1.1.4 2.3.6 3.6.6.6 0 1 .4 1 1V20c0 .6-.4 1-1 1C10.6 21 3 13.4 3 4c0-.6.4-1 1-1h3.5c.6 0 1 .4 1 1 0 1.3.2 2.5.6 3.6.1.3 0 .7-.2 1l-2.3 2.2z"/>
          </svg>
          <span>0427309581</span>
        </li>
        <li class="contact-item">
          <span class="social-mark" aria-hidden="true"></span>
          <span>Torvane PT</span>
        </li>
      </ul>
    </div>
  </article>
</main>
</body>
</html>
```